Iron and home washing service

I provide I home iron and washing service for adult and kids clothes on a smoke pet free environment. I can collect and offer a next day delivery. Or same day depend on items and volume. I offer competitive frendly and reliable service and price. I charge by weight £4,50 / kg. approx 5 items =1 kg minimum for collection.

```html
<!DOCTYPE html>
<html lang="en">
<head>
<meta charset="utf-8">
<title>Iron &amp; Home Washing Service Flyer</title>
<link rel="stylesheet" href="https://fonts.googleapis.com/css2?family=Anton&family=Montserrat:wght@600;700&family=Source+Sans+3:ital,wght@0,400;0,700;1,700&family=Oswald:wght@500&display=swap">
<style>
  :root {
    --page-bg: #e8e5e1;
    --sky-top: #4fa3e3;
    --sky-mid: #6bb6ec;
    --sky-low: #a9d6f5;
    --banner-blue: #1b6fc2;
    --banner-shadow: #0d3f78;
    --ink: #1e1e1e;
    --white: #ffffff;
    --crimson: #c41f3e;
    --footer: #0f0f0f;
  }
  * { margin: 0; padding: 0; box-sizing: border-box; }
  html, body { width: 1200px; height: 857px; overflow: hidden; background: var(--page-bg); }
  .flyer {
    position: absolute; left: 313px; top: 23px; width: 574px; height: 810px;
    background: linear-gradient(180deg, var(--sky-top) 0%, var(--sky-mid) 45%, var(--sky-low) 90%);
    overflow: hidden; box-shadow: 0 6px 18px rgba(0,0,0,.25);
  }
  .title-bar { position: absolute; top: 110px; height: 16px; background: var(--white); }
  .title-bar.left { left: 0; width: 34px; }
  .title-bar.right { left: 541px; width: 33px; }
  .title-box {
    position: absolute; left: 34px; top: 51px; width: 507px; height: 137px;
    border: 1.5px solid var(--white); text-align: center; color: var(--white);
  }
  .kicker {
    position: absolute; left: 50%; top: -18px; transform: translateX(-50%);
    background: var(--sky-top); padding: 0 10px; white-space: nowrap;
    font: 600 31px/36px "Montserrat", sans-serif; display: flex; align-items: center; gap: 10px;
  }
  .kicker .dot { width: 16px; height: 16px; border-radius: 50%; background: var(--white); }
  .headline { position: absolute; left: 0; right: 0; top: 14px; font: 400 62px/76px "Anton", sans-serif; letter-spacing: .5px; }
  .subline { position: absolute; left: 0; right: 0; top: 90px; font: 700 30px/36px "Montserrat", sans-serif; letter-spacing: .5px; }
  .features { position: absolute; left: 176px; top: 201px; list-style: none; color: var(--ink); font: 400 20px/26px "Source Sans 3", sans-serif; }
  .features li { position: relative; padding-left: 15px; margin-bottom: 4px; }
  .features li::before { content: ""; position: absolute; left: 0; top: 9px; width: 8px; height: 8px; border-radius: 50%; background: var(--ink); }
  .features strong { font-weight: 700; }
  .clothesline { position: absolute; left: 0; top: 260px; }
  .offer-banner {
    position: absolute; left: 173px; top: 297px; width: 343px; height: 56px;
    background: var(--banner-blue); color: var(--white);
    font: italic 700 19px/20px "Source Sans 3", sans-serif; padding: 7px 0 0 14px;
  }
  .offer-banner::before { content: ""; position: absolute; left: -6px; top: 0; width: 6px; height: 44px; background: var(--banner-shadow); }
  .offer-banner span { display: block; }
  .offer-banner span + span { padding-left: 8px; }
  .product-photo {
    position: absolute; left: 0; top: 356px; width: 574px; height: 382px;
    background: linear-gradient(90deg, rgba(60,160,170,.35) 0%, rgba(169,214,245,0) 35%, rgba(240,90,160,.45) 70%, rgba(230,60,130,.6) 100%),
                linear-gradient(180deg, rgba(255,255,255,0) 80%, #8b7b6e 95%);
  }
  .price-card {
    position: absolute; left: 95px; top: 560px; width: 228px; height: 150px;
    background: var(--white); transform: rotate(-5deg); padding: 8px;
    box-shadow: 0 2px 6px rgba(0,0,0,.2);
  }
  .price-card .inner {
    width: 100%; height: 100%; border: 1px solid var(--crimson); color: var(--crimson);
    text-align: center; padding-top: 12px; font: 400 17px/22px "Source Sans 3", sans-serif;
  }
  .price-card .price-title { font: 500 23px/28px "Oswald", sans-serif; letter-spacing: .3px; }
  .footer {
    position: absolute; left: 0; bottom: 0; width: 574px; height: 72px; background: var(--footer);
    color: var(--white); text-align: center; font: 700 33px/72px "Montserrat", sans-serif; letter-spacing: 1px;
  }
</style>
</head>
<body>
  <main class="flyer">
    <div class="product-photo" role="img" aria-label="Steam iron standing beside a tall stack of folded colourful clothes and towels with daisies on a wooden table"></div>

    <div class="title-bar left"></div>
    <div class="title-bar right"></div>
    <header class="title-box">
      <div class="kicker"><span class="dot"></span>Iron &amp; Home<span class="dot"></span></div>
      <h1 class="headline">Washing Service</h1>
      <p class="subline">For Adult &amp; Kids Clothes</p>
    </header>

    <ul class="features">
      <li>On a Smoke Pet <strong>FREE</strong> Environment</li>
      <li>Collect &amp; Offer a Next day Delivery Or<br>Same day Depend on Items &amp; Volume</li>
    </ul>

    <svg class="clothesline" width="574" height="60" viewBox="0 0 574 60" aria-hidden="true">
      <path d="M0 18 Q 300 48 574 14" fill="none" stroke="#ffffff" stroke-width="1.5"/>
    </svg>

    <div class="offer-banner">
      <span>OFFER COMPETITIVE FRENDLY &amp;</span>
      <span>RELIABLE SERVICE &amp; PRICE</span>
    </div>

    <aside class="price-card">
      <div class="inner">
        <div class="price-title">CHARGE BY WEIGHT</div>
        <div>£4,50 / kg.</div>
        <div>Approx 5 Items =1 kg</div>
        <div>Minimum for Collection</div>
      </div>
    </aside>

    <footer class="footer">CALL US: 000.000.0000</footer>
  </main>
</body>
</html>
```